Post card for landscape service

Velmora Property Management**FEATURED SERVICE*** Weekly Lawn mowing service starting at $15/ cutting ****other services****landscape servicespring and fall clean uplawn and flowerbed care (pest and weed control)fertilizing plantingand moreCall for a Free estimate!!10% off first months service with signed contract

Please make double sided ( a front and a back)

Target Market(s)

home owners

Industry/Entity Type

Landscape

Requirements
Must have
• please feture the weekly lawn mowing service and then list the other sevices
• contact info... can be found on business card that was uploaded.
• must say residential services
Should not have
• please dont list reo management

```html
<!DOCTYPE html>
<html lang="en">
<head>
<meta charset="utf-8">
<title>Velmora Property Management – Postcard</title>
<link rel="stylesheet" href="https://fonts.googleapis.com/css2?family=Open+Sans:ital,wght@0,400;0,700;1,700&family=Tinos&display=swap">
<style>
  :root {
    --ink: #1d1d1b;
    --white: #ffffff;
    --grass: #3aa81e;
    --forest-dark: #2a2418;
    --forest-mid: #6b5a33;
    --forest-light: #c9c27a;
    --leaf-rust: #8a2f16;
    --leaf-deep: #5e1e0e;
    --phone-bg: rgba(20, 18, 14, 0.55);
    --rule: #333333;
  }
  * { box-sizing: border-box; margin: 0; padding: 0; }
  html, body { width: 1200px; height: 431px; overflow: hidden; background: var(--white); }
  body { font-family: "Open Sans", Arial, sans-serif; color: var(--ink); }

  .postcard { position: relative; width: 1200px; height: 431px; display: flex; }

  /* Front */
  .front { position: relative; width: 600px; height: 431px; overflow: hidden; color: var(--white); }
  .forest-photo {
    position: absolute; inset: 0;
    background:
      radial-gradient(ellipse 22% 40% at 50% 38%, var(--forest-light) 0%, rgba(201,194,122,0) 100%),
      linear-gradient(180deg, var(--forest-dark) 0%, var(--forest-mid) 38%, #4a3520 60%, var(--leaf-rust) 78%, var(--leaf-deep) 100%);
  }
  .headline {
    position: absolute; top: 26px; left: 40px; width: 520px;
    text-align: center; font-weight: 700; font-size: 21px; line-height: 1.3;
    text-shadow: 0 1px 3px rgba(0,0,0,.6);
  }
  .cta {
    position: absolute; top: 150px; left: 0; width: 600px;
    text-align: center; font-weight: 700; font-style: italic; font-size: 21px;
    text-shadow: 0 1px 3px rgba(0,0,0,.6);
  }
  .phone {
    position: absolute; top: 178px; left: 196px; width: 208px; height: 36px;
    background: var(--phone-bg); text-align: center;
    font-weight: 700; font-style: italic; font-size: 27px; line-height: 36px;
  }
  .offer {
    position: absolute; top: 224px; left: 0; width: 600px;
    text-align: center; font-weight: 700; font-style: italic; font-size: 14px;
    text-shadow: 0 1px 3px rgba(0,0,0,.7);
  }
  .brand-tile {
    position: absolute; left: 14px; top: 310px; width: 80px; height: 80px;
    background: var(--white); color: var(--ink);
    display: flex; flex-direction: column; align-items: center; justify-content: center; gap: 5px;
  }
  .brand-dot { width: 42px; height: 42px; border-radius: 50%; background: var(--ink); }
  .brand-name { font-size: 7.5px; font-weight: 400; white-space: nowrap; }
  .service-list {
    position: absolute; left: 98px; top: 301px; list-style: none;
    font-weight: 700; font-style: italic; font-size: 12.5px; line-height: 15px;
    text-shadow: 0 1px 2px rgba(0,0,0,.7);
  }
  .contact-band {
    position: absolute; left: 0; bottom: 0; width: 600px; height: 37px;
    background: var(--grass); display: flex; justify-content: space-between; align-items: center;
    padding: 0 17px 4px 18px; font-weight: 700; font-style: italic; font-size: 14px;
  }

  /* Back */
  .back { position: relative; width: 600px; height: 431px; background: var(--white); }
  .back-title {
    position: absolute; left: 178px; top: 30px; width: 200px; text-align: center;
    font-family: "Tinos", "Times New Roman", serif; font-weight: 400; font-size: 28px; letter-spacing: .5px;
  }
  .back-brand {
    position: absolute; left: 228px; top: 68px; width: 100px;
    display: flex; flex-direction: column; align-items: center; gap: 3px;
  }
  .back-brand .brand-dot { width: 44px; height: 44px; }
  .back-brand .brand-name { font-size: 7px; }
  .divider { position: absolute; left: 278px; top: 136px; width: 1px; height: 220px; background: var(--rule); }
  .stamp-box {
    position: absolute; left: 490px; top: 19px; width: 96px; height: 111px;
    border: 1px solid var(--rule); text-align: center;
    padding-top: 26px; font-size: 12.5px; line-height: 16px; text-transform: uppercase;
  }
  .back-services { position: absolute; left: 22px; top: 107px; list-style: none; font-size: 10.5px; line-height: 12.8px; }
  .back-services .group { font-size: 11px; }
  .back-services .address { font-weight: 700; }
</style>
</head>
<body>
<main class="postcard">
  <section class="front">
    <div class="forest-photo" role="img" aria-label="Photo of an autumn forest path lined with tall trees and red fallen leaves"></div>
    <h1 class="headline">Having trouble with weekly lawn mowing service?</h1>
    <p class="cta">Give us a call for a Free Estimate!</p>
    <p class="phone">800-555-0142</p>
    <p class="offer">10% off first month's service with signed contract</p>
    <div class="brand-tile">
      <span class="brand-dot"></span>
      <span class="brand-name">Velmora Property</span>
    </div>
    <ul class="service-list">
      <li>RESIDENTIAL SERVICES</li>
      <li>Weekly Lawn Mowing from $15/cutting</li>
      <li>Landscape Service &amp; Planting</li>
      <li>Spring and Fall Clean Up</li>
      <li>Lawn &amp; Flowerbed Care</li>
      <li>Fertilizing and More</li>
    </ul>
    <footer class="contact-band">
      <span class="email">hello@velmoraproperty.com</span>
      <span class="address">Brookhaven, NJ 08800 PO Box 214</span>
    </footer>
  </section>

  <section class="back">
    <h2 class="back-title">POSTCARD</h2>
    <div class="back-brand">
      <span class="brand-dot"></span>
      <span class="brand-name">Velmora Property</span>
    </div>
    <ul class="back-services">
      <li class="group">RESIDENTIAL SERVICES</li>
      <li>Weekly Lawn Mowing from $15/cutting</li>
      <li>Landscape Service &amp; Planting</li>
      <li>Spring and Fall Clean Up</li>
      <li>Lawn &amp; Flowerbed Care (pest &amp; weed control)</li>
      <li>Fertilizing and More</li>
      <li class="address">Brookhaven,&nbsp;&nbsp; NJ 08800&nbsp; -&nbsp; PO Box 214</li>
    </ul>
    <div class="divider"></div>
    <div class="stamp-box">Place<br>Stamp<br>Here</div>
  </section>
</main>
</body>
</html>
```